New Business Card Design For Re-Branded Company (New Logo)

We recently switched our DBA and had a new logo designed. We now need new business cards made around our new logo. We would like to stick with the color scheme in our logo: White, Orange, and Blue. We want to see original bold designs that reflect our position in the solar energy sector but we prefer simple over complicated.

We are curious about vertical designs so if you can translate your design onto a vertical layout we would be open to look at it. We especially like a few designs we have seen on here that are vertical with a black or very dark gray background. They have our logo on one side and then the normal vertical business card on the other side.

I have included a screenshot of one of the samples we like, labeled sample.jpg and a file we were given as an example of our logo on a dark background.

At the same time we are satisfied to stay with what we have always had in a horizontal format. If it's not a lot of extra work for you, designs that are submitted in both horizontal and vertical formats will be greatly appreciated.

Please submit your original, bold, clean designs for consideration. Contact us with any questions or comments that may arise.

Thank you and Good Luck,

RT

```html
<!DOCTYPE html>
<html lang="en">
<head>
<meta charset="utf-8">
<title>Brightwell Solar – Business Card</title>
<link rel="stylesheet" href="https://fonts.googleapis.com/css2?family=Open+Sans:wght@400;700;800&display=swap">
<style>
  :root {
    --stage: #e9e6e1;
    --card: #2b2b2d;
    --orange: #f0a228;
    --orange-deep: #e08a1e;
    --blue: #1d9ad6;
    --white: #ffffff;
  }
  * { box-sizing: border-box; margin: 0; padding: 0; }
  html, body { width: 1200px; height: 780px; overflow: hidden; background: var(--stage); }
  .canvas {
    position: relative; width: 1200px; height: 780px;
    font-family: "Open Sans", sans-serif;
  }
  .card {
    position: absolute; top: 110px; width: 320px; height: 560px;
    background: var(--card); border-radius: 4px; overflow: hidden;
    box-shadow: 0 10px 28px rgba(0,0,0,.25);
  }
  .card--front { left: 230px; }
  .card--back { left: 650px; }

  .brand {
    display: flex; align-items: center; gap: 8px;
    font-family: "Open Sans", sans-serif; font-weight: 800;
    color: var(--orange); letter-spacing: .3px; white-space: nowrap;
  }
  .brand__dot { flex: none; border-radius: 50%; background: var(--blue); }

  .card--front .brand { position: absolute; top: 64px; left: 0; right: 0; justify-content: center; font-size: 23px; }
  .card--front .brand__dot { width: 20px; height: 20px; }

  .person { position: absolute; top: 150px; left: 0; right: 0; text-align: center; }
  .person__name { color: var(--orange); font-weight: 800; font-size: 20px; letter-spacing: .5px; }
  .person__role { color: var(--white); font-size: 15px; margin-top: 2px; }

  .contact { position: absolute; top: 222px; left: 42px; right: 20px; color: var(--white); font-size: 15px; line-height: 1.45; }
  .contact__line { display: flex; align-items: center; gap: 8px; }
  .contact__icon { flex: none; width: 18px; height: 18px; }
  .contact__address { margin-top: 10px; }

  .front-band {
    position: absolute; left: 0; right: 0; bottom: 0; height: 170px;
    background: linear-gradient(180deg, var(--card) 0%, var(--blue) 28%, var(--orange-deep) 55%, var(--orange) 100%);
  }

  .card--back .brand {
    position: absolute; left: 160px; top: 280px;
    transform: translate(-50%, -50%) rotate(90deg);
    font-size: 38px;
  }
  .card--back .brand__dot { width: 32px; height: 32px; }
</style>
</head>
<body>
<main class="canvas">

  <section class="card card--front" aria-label="Card front">
    <div class="brand"><span class="brand__dot"></span>BRIGHTWELL SOLAR</div>

    <div class="person">
      <p class="person__name">EMPLOYEE NAME</p>
      <p class="person__role">Owner</p>
    </div>

    <div class="contact">
      <p class="contact__line">
        <svg class="contact__icon" viewBox="0 0 18 18" aria-hidden="true">
          <rect width="18" height="18" rx="2" fill="var(--orange)"/>
          <path d="M4 6c0-1.5 2.2-2.5 5-2.5S14 4.5 14 6v1.2h-2.6V6.1H6.6v1.1H4z M5 9h8l1 5H4z" fill="var(--card)"/>
        </svg>
        123-456-7890
      </p>
      <p class="contact__line">
        <svg class="contact__icon" viewBox="0 0 18 18" aria-hidden="true">
          <rect width="18" height="18" rx="2" fill="var(--orange)"/>
          <rect x="5" y="3" width="8" height="12" rx="1.5" fill="var(--card)"/>
          <rect x="6.5" y="5" width="5" height="6" fill="var(--orange)"/>
        </svg>
        123-456-7890
      </p>
      <p>your@youremail.com</p>
      <p class="contact__address">1111 youraddress Lane<br>Aldale TX 00000 USA</p>
    </div>

    <div class="front-band" role="img" aria-label="Decorative swoosh band in blue and orange"></div>
  </section>

  <section class="card card--back" aria-label="Card back">
    <div class="brand"><span class="brand__dot"></span>BRIGHTWELL SOLAR</div>
  </section>

</main>
</body>
</html>
```